Lanna Cove Villa - Rental Villa Website

I have a villa for rent in Thailand and require a website - i need to demo pictures/walk through video, local attractions, villa facilities description plus seaonal rates and online booking.

Industry/Entity Type

Rental

Coding

Coded - Design and coding required

```html
<!DOCTYPE html>
<html lang="en">
<head>
<meta charset="utf-8">
<title>Lanna Cove Villa – Holiday Rental</title>
<link rel="stylesheet" href="https://fonts.googleapis.com/css2?family=Lato:wght@400;700&family=Dancing+Script:wght@700&family=Roboto:wght@400;500&display=swap">
<style>
:root{
  --brown:#5a4507;
  --brown-dark:#4a3905;
  --gold-bar:#f2dc8b;
  --ink:#222;
  --ink-soft:#555;
  --page:#f6f6f6;
  --panel:#f1f1f1;
  --white:#fff;
  --footer:#111;
  --line:#d9d9d9;
}
*{box-sizing:border-box;margin:0;padding:0}
html,body{width:1200px;height:3139px;overflow:hidden}
body{position:relative;background:var(--page);font-family:'Lato',sans-serif;color:var(--ink)}
.abs{position:absolute}
.wrap{position:absolute;left:98px;width:1004px}

/* top bar */
.topbar{top:0;height:44px;background:var(--gold-bar);display:flex;align-items:center;padding:0 22px;font-size:11px;font-weight:700}
.topbar .addr{display:flex;align-items:center;gap:8px}
.social{display:flex;gap:9px}
.topbar .social{position:absolute;left:452px;top:9px}
.sq{width:25px;height:25px;background:var(--white);display:block}
.topbar .book{position:absolute;right:38px;top:8px;width:80px;height:28px;background:var(--white);font-size:12px;display:flex;align-items:center;justify-content:center;font-weight:400}

/* header */
.header{top:44px;height:135px;background:var(--white)}
.navstrip{position:absolute;left:0;right:0;top:44px;height:45px;background:linear-gradient(#fbfbfb,#e3e3e3);border-bottom:1px solid #cfcfcf}
.menu{position:absolute;right:0;top:44px;height:45px;display:flex;font-size:14px;list-style:none}
.menu li{padding:0 20px;display:flex;align-items:center}
.menu li.active{background:linear-gradient(#d6d6d6,#eeeeee)}
.brand{position:absolute;left:24px;top:13px;width:166px;height:148px;background:var(--white);box-shadow:0 2px 6px rgba(0,0,0,.2);display:flex;align-items:center;justify-content:center;text-align:center;font-weight:700;font-size:20px;line-height:1.2;color:var(--brown);z-index:2}

/* hero */
.hero{top:179px;height:604px;background:linear-gradient(135deg,#6f6a63 0%,#bdb8b0 35%,#8b7f74 60%,#3f3530 100%)}
.arrow{position:absolute;top:259px;width:36px;height:36px;background:var(--white);border-radius:3px;display:flex;align-items:center;justify-content:center}
.booking{position:absolute;left:30px;top:484px;width:945px;height:74px;background:var(--white);border-radius:37px;box-shadow:0 0 0 6px rgba(255,255,255,.4);display:flex;align-items:center;padding-left:14px}
.booking .label{font-size:15px;color:var(--brown);margin-right:10px}
.chev{font-size:14px;color:var(--brown);margin:0 8px;font-weight:700}
.field{height:38px;border:1px solid var(--line);border-radius:3px;display:flex;align-items:center;justify-content:space-between;padding:0 8px;font-size:12px;color:#999}
.booking .go{position:absolute;right:4px;top:0;width:122px;height:74px;background:var(--brown);border-radius:0 37px 37px 0;color:var(--white);font-size:12px;font-weight:700;display:flex;align-items:center;justify-content:center}

/* section titles */
.title{position:absolute;left:0;right:0;text-align:center;font-size:28px;color:var(--brown);text-transform:uppercase}
.title::after{content:"";display:block;width:100px;height:2px;background:var(--brown);margin:8px auto 0}
.script{position:absolute;left:0;right:0;text-align:center;font-family:'Dancing Script',cursive;font-size:22px;color:var(--brown)}

/* reserve */
.reserve{top:783px;height:280px;background:var(--panel)}
.stat{position:absolute;top:160px;display:flex;gap:14px}
.stat .box{width:59px;height:59px;background:var(--brown);color:var(--white);display:flex;align-items:center;justify-content:center;font-size:30px;box-shadow:0 3px 0 var(--brown-dark)}
.stat .big{font-size:24px;margin-top:4px}
.stat .small{font-size:12px;color:var(--ink-soft);margin-top:4px}

/* features */
.features{top:1063px;height:495px;background:var(--white)}
.feature{position:absolute;top:53px;width:280px;text-align:center}
.photo-circle{width:206px;height:206px;border-radius:50%;margin:0 auto;border:8px solid var(--white);box-shadow:0 0 0 2px #e2e2e2}
.feature h3{margin-top:22px;font-size:21px;font-weight:400;color:var(--brown)}
.feature .rule{height:1px;background:var(--line);margin:8px 0 0}
.feature .star{font-size:14px;color:var(--ink);margin-top:2px}
.feature p{font-size:13px;line-height:17px;color:var(--brown);margin-top:6px}
.btn{display:inline-flex;align-items:center;justify-content:center;height:32px;padding:0 24px;background:var(--brown);color:var(--white);border-radius:16px;font-size:13px;text-transform:uppercase;margin-top:14px}

/* details */
.details{top:1558px;height:610px;background:var(--panel)}
.amenity{position:absolute;top:178px;display:flex;align-items:center;gap:20px;font-size:17px;color:var(--ink)}
.details p.copy{position:absolute;top:256px;width:467px;font-size:13px;line-height:17px;color:var(--brown);text-align:justify}
.shot{position:absolute;top:345px;width:219px;height:219px}

/* inquiry */
.inquiry{top:2168px;height:152px;background:var(--brown);text-align:center;color:var(--white)}
.inquiry p{font-size:21px;margin-top:38px}
.inquiry .pill{display:inline-flex;align-items:center;justify-content:center;width:188px;height:33px;background:var(--white);color:var(--brown);border-radius:17px;font-size:13px;margin-top:18px}

/* map & footer */
.map{left:0;top:2362px;width:1200px;height:349px;background:linear-gradient(160deg,#c8ddf0 0%,#e6e4d6 30%,#cfe0b8 55%,#e8e5d9 75%,#b9d4ec 100%)}
.footer{left:0;top:2711px;width:1200px;height:282px;background:var(--footer)}
.foot-brand{position:absolute;left:150px;top:40px;width:220px;text-align:center;font-weight:700;font-size:24px;color:#c9a83b}
.foot-text{position:absolute;left:122px;top:170px;width:222px;font-size:12px;line-height:15px;color:var(--white);text-align:justify}
.gallery{position:absolute;left:857px;top:62px}
.gallery h4{font-family:'Roboto',sans-serif;font-weight:400;font-size:27px;color:var(--white)}
.thumbs{display:grid;grid-template-columns:repeat(3,67px);gap:8px;margin-top:14px}
.thumbs span{height:67px;display:block}
.contact{left:368px;top:2631px;width:463px;height:362px;background:var(--brown);font-family:'Roboto',sans-serif;color:var(--white);text-align:center;z-index:3;border-radius:4px 4px 0 0}
.contact h2{font-weight:400;font-size:26px;margin-top:38px}
.contact .sub{font-size:12px;margin-top:2px}
.input{position:absolute;left:80px;width:300px;height:46px;border:1px solid #d9c98f;border-radius:3px;font-size:11px;text-align:left;padding:14px 16px}
.contact .send{position:absolute;left:175px;top:343px;width:112px;height:36px;background:var(--white);color:var(--ink);font-size:11px;font-weight:500;display:flex;align-items:center;justify-content:center;border-radius:2px}
.bottombar{left:0;top:2993px;width:1200px;height:80px;background:var(--brown);color:var(--white);font-size:12px}
.bottombar .item{position:absolute;top:33px;display:flex;align-items:center;gap:12px}
.bottombar .social{position:absolute;left:979px;top:27px}
.bottombar .social .sq{width:27px;height:27px;background:none;border:1px solid var(--white);border-radius:2px}
.copyright{left:0;top:3073px;width:1200px;height:66px;background:var(--footer);color:var(--white);font-size:12px;text-align:center;line-height:66px}
</style>
</head>
<body>

<div class="wrap topbar">
  <div class="addr">
    <svg width="12" height="14" viewBox="0 0 12 14"><path d="M6 0a5 5 0 0 0-5 5c0 4 5 9 5 9s5-5 5-9a5 5 0 0 0-5-5zm0 7a2 2 0 1 1 0-4 2 2 0 0 1 0 4z" fill="#222"/></svg>
    <span>88 Palm Lane, Cove Town, Thailand</span>
  </div>
  <div class="social"><span class="sq"></span><span class="sq"></span><span class="sq"></span></div>
  <div class="book">BOOK</div>
</div>

<header class="wrap header">
  <div class="navstrip"></div>
  <div class="brand">Lanna Cove<br>Villa</div>
  <ul class="menu">
    <li class="active">Home</li><li>About Us</li><li>Gallery</li><li>Reservation</li><li>Blog</li><li>Contact Us</li>
  </ul>
</header>

<section class="wrap hero">
  <div class="abs" style="inset:0" role="img" aria-label="Villa bedroom with bed, artwork on the wall and garden view through the door"></div>
  <div class="arrow" style="left:28px"><svg width="12" height="14" viewBox="0 0 12 14"><path d="M9 1 3 7l6 6" stroke="#222" stroke-width="2" fill="none"/></svg></div>
  <div class="arrow" style="right:26px"><svg width="12" height="14" viewBox="0 0 12 14"><path d="m3 1 6 6-6 6" stroke="#222" stroke-width="2" fill="none"/></svg></div>
  <form class="booking">
    <span class="label">Book A Room</span><span class="chev">»</span>
    <div class="field" style="width:178px">Check-in date <svg width="13" height="13" viewBox="0 0 13 13"><rect x="1" y="2" width="11" height="10" fill="none" stroke="#999"/><path d="M1 5h11" stroke="#999"/></svg></div><span class="chev">»</span>
    <div class="field" style="width:178px">Check-out date <svg width="13" height="13" viewBox="0 0 13 13"><rect x="1" y="2" width="11" height="10" fill="none" stroke="#999"/><path d="M1 5h11" stroke="#999"/></svg></div><span class="chev">»</span>
    <div class="field" style="width:110px">Adults <span>⇕</span></div><span class="chev">»</span>
    <div class="field" style="width:110px">Childrens <span>⇕</span></div>
    <div class="go">BOOK NOW !</div>
  </form>
</section>

<section class="wrap reserve">
  <h2 class="title" style="top:40px;font-weight:400">Reserve your villa now</h2>
  <p class="script" style="top:90px">Click to calculate the price and book your holiday. Show calendar</p>
  <div class="stat" style="left:26px"><div class="box">10</div><div><div class="big">Check In</div><div class="small">Tue, Feb 2015</div></div></div>
  <div class="stat" style="left:272px"><div class="box"><svg width="30" height="28" viewBox="0 0 30 28"><rect x="2" y="4" width="26" height="22" fill="none" stroke="#fff" stroke-width="2"/><rect x="2" y="4" width="26" height="6" fill="#fff"/><path d="M8 14h14M8 19h14M12 10v16M18 10v16" stroke="#fff" stroke-width="1.5"/></svg></div><div><div class="big">Check Out</div><div class="small">Check In First</div></div></div>
  <div class="stat" style="left:515px"><div class="box">1</div><div><div class="big">Guests</div><div class="small">Max Five</div></div></div>
  <div class="stat" style="left:761px"><div class="box" style="font-size:20px">€ 10</div><div><div class="big">From</div><div class="small">Tax Excl.</div></div></div>
</section>

<section class="wrap features">
  <article class="feature" style="left:36px">
    <div class="photo-circle" role="img" aria-label="Bedroom interior" style="background:linear-gradient(135deg,#8a8078,#d6d0c6,#5c524a)"></div>
    <h3>ROOMS</h3><div class="rule"></div><div class="star">★</div>
    <p>Sed do eiuunt mod tempor incididunt labore et amor magi aliqua. Ut enim minim veniam, quis nostrud. Lorem ipsum amor sit amet, consect.</p>
    <span class="btn">Explore the rooms</span>
  </article>
  <article class="feature" style="left:362px">
    <div class="photo-circle" role="img" aria-label="Villa exterior with tiled roof and garden" style="background:linear-gradient(135deg,#5f7a4a,#9b8a7c,#3a3a36)"></div>
    <h3>OUR VILLA</h3><div class="rule"></div><div class="star">★</div>
    <p>Sed do eiuunt mod tempor incididunt labore et amor magi aliqua. Ut enim minim veniam, quis nostrud. Lorem ipsum amor sit amet, consect.</p>
    <span class="btn">Visit a villa</span>
  </article>
  <article class="feature" style="left:688px">
    <div class="photo-circle" role="img" aria-label="Infinity swimming pool" style="background:linear-gradient(180deg,#b9bcb6,#6f9990,#3d6b62)"></div>
    <h3>SWIMING PULL</h3><div class="rule"></div><div class="star">★</div>
    <p>Sed do eiuunt mod tempor incididunt labore et amor magi aliqua. Ut enim minim veniam, quis nostrud. Lorem ipsum amor sit amet, consect.</p>
    <span class="btn">Visit a swiming pull</span>
  </article>
</section>

<section class="wrap details">
  <h2 class="title" style="top:40px;font-weight:400">Villa details</h2>
  <p class="script" style="top:96px">A short list of the main features of the holiday home</p>
  <div class="amenity" style="left:30px"><svg width="40" height="34" viewBox="0 0 40 34"><path d="M20 2 2 18h5v14h10v-9h6v9h10V18h5z" fill="#5a4507"/></svg>200 sq ft.</div>
  <div class="amenity" style="left:276px"><svg width="40" height="32" viewBox="0 0 40 32"><path d="M8 4h24l5 12v12h-6v-4H9v4H3V16z" fill="#5a4507"/><path d="M10 8h20l3 8H7z" fill="#f1f1f1"/><circle cx="10" cy="20" r="2.5" fill="#f1f1f1"/><circle cx="30" cy="20" r="2.5" fill="#f1f1f1"/></svg>CAR GARAGE</div>
  <div class="amenity" style="left:520px"><svg width="36" height="34" viewBox="0 0 36 34"><ellipse cx="18" cy="23" rx="9" ry="8" fill="#5a4507"/><circle cx="7" cy="13" r="4" fill="#5a4507"/><circle cx="14" cy="6" r="4" fill="#5a4507"/><circle cx="22" cy="6" r="4" fill="#5a4507"/><circle cx="29" cy="13" r="4" fill="#5a4507"/></svg>PETS ALLOWED</div>
  <div class="amenity" style="left:762px"><svg width="40" height="32" viewBox="0 0 40 32"><path d="M3 11a24 24 0 0 1 34 0M9 17a16 16 0 0 1 22 0M15 23a8 8 0 0 1 10 0" stroke="#5a4507" stroke-width="4" fill="none" stroke-linecap="round"/><circle cx="20" cy="28" r="3" fill="#5a4507"/></svg>FREE WIFI</div>
  <p class="copy" style="left:24px">The holiday home has a stunning 270 degree sea view and is located in a perfectly quiet place. It's away from the traffic but enough near to the town centre to enjoy its services.</p>
  <p class="copy" style="left:515px">The holiday home has a stunning 270 degree sea view and is located in a perfectly quiet place. It's away from the traffic but enough near to the town centre to enjoy its services.</p>
  <div class="shot" style="left:24px;background:linear-gradient(135deg,#d8d4cc,#8c8278,#4a423b)" role="img" aria-label="Bedroom with artwork"></div>
  <div class="shot" style="left:270px;background:linear-gradient(135deg,#6f8a58,#9a8478,#3e3d39)" role="img" aria-label="Villa roof and garden"></div>
  <div class="shot" style="left:515px;background:linear-gradient(160deg,#8a6a4e,#c8c2b4,#5d6f4d)" role="img" aria-label="Covered terrace with sea view"></div>
  <div class="shot" style="left:761px;background:linear-gradient(180deg,#b7bab4,#7ea59c,#40706a)" role="img" aria-label="Swimming pool"></div>
</section>

<section class="wrap inquiry">
  <p>Any inquiries? Call us on 0870 555 214. Psst... you can also book online! Click on the button below...</p>
  <span class="pill">BOOK ONLINE NOW</span>
</section>

<div class="abs map" role="img" aria-label="Map of Thailand and surrounding region showing the villa location"></div>

<footer class="abs footer">
  <div class="foot-brand">Lanna Cove<br>Villa</div>
  <p class="foot-text">Ut wisi enim ad minim veniam, quis nostrud tation ullamcorper suscipit loborts nisl ut ali ea commodo consequat. Lorem ipsum dolor et, consectetuer adipiscng elitre.</p>
  <div class="gallery">
    <h4>Gallery</h4>
    <div class="thumbs">
      <span role="img" aria-label="Pool" style="background:linear-gradient(#9fb3ac,#4f7a70)"></span>
      <span role="img" aria-label="Bedroom" style="background:linear-gradient(#8d8178,#3c342e)"></span>
      <span role="img" aria-label="Terrace" style="background:linear-gradient(#7a6a56,#9fb3ac)"></span>
      <span role="img" aria-label="Pool deck" style="background:linear-gradient(#b9bcb6,#5d8a80)"></span>
      <span role="img" aria-label="Villa exterior" style="background:linear-gradient(#6e5a46,#2f2a26)"></span>
      <span role="img" aria-label="Pool view" style="background:linear-gradient(#a9b5b0,#3f6d64)"></span>
    </div>
  </div>
</footer>

<form class="abs contact">
  <h2>CONTACT US</h2>
  <p class="sub">Aenean commodo ligula egt tash pisncing</p>
  <div class="input" style="top:116px">Enter Your Name</div>
  <div class="input" style="top:169px">Enter Your Email</div>
  <div class="input" style="top:223px;height:104px">Message</div>
  <div class="send">SUBMIT NOW</div>
</form>

<div class="abs bottombar">
  <div class="item" style="left:126px"><svg width="14" height="14" viewBox="0 0 14 14"><circle cx="7" cy="7" r="6.5" fill="#fff"/><path d="M1 7h12M7 1c-3 3-3 9 0 12M7 1c3 3 3 9 0 12" stroke="#5a4507" fill="none"/></svg>stay@lannacovevilla.example</div>
  <div class="item" style="left:392px"><svg width="14" height="14" viewBox="0 0 14 14"><path d="M3 1 5.5 4 4 6a8 8 0 0 0 4 4l2-1.5 3 2.5-1.5 2C6 13 1 8 1 2.5z" fill="#fff"/></svg>+12 5550 123456</div>
  <div class="social"><span class="sq"></span><span class="sq"></span><span class="sq"></span></div>
</div>

<div class="abs copyright">© Copyright 2015 &nbsp; | &nbsp; Lanna Cove Villa &nbsp; | &nbsp; All Rights Reserved</div>

</body>
</html>
```